Marlow Yardcraft need a flyer - A6 - Double sided

We need a flyer that will engage potential customer in need for gardening services. We offer high quality gardening services spanning from lawn mowing and weeding to soil improvement to tree pruning and so on.
I would like a double sided flyer A6 size. I trust your expert touch in terms of lay out but the general idea I had was to have one side with the logo, a catchy picture (or more), the website/phone number/address and on the flip side a little more text focusing on the client perspective with statement such as 'Let us do the hard work so that you can enjoy your garden' (obviously the wording isn't my strongest skill) but the idea is to get into the customer perspective;
I would also like to list all the service we can offer such as but not limited to weeding, pruning, lawn care, green waste disposal, soil improvement, hedging, edging, lawn mowing,...
Happy for you to use any picture free of right from the internet if necessary

Target Market(s)

Home owner & Businesses

Industry/Entity Type

Landscape Gardening

Requirements
Must have
• website - http://yardcraft-marlow.com.au (feel free to browse the website to get ideas on color theme and overall look)
• phone number - (08) 6341 2705
Nice to have
• a list of services on offer
• phone number and website
• being customer perspective focused (the benefits for the customer) - perhaps on the flip side some text like 'highly trained and experienced landscape gardeners so that the job is done perfectly every time', 'always carrying all range of commercial grade tools so that we can tackle any job', 'Experienced gardeners so that the job is achieve faster' (it doesn't have to be in those exact words as I trust that you may be expert in wording as well as designers?)

```html
<!DOCTYPE html>
<html lang="en">
<head>
<meta charset="utf-8">
<title>Marlow Yardcraft – A6 Flyer, Front and Back</title>
<link href="https://fonts.googleapis.com/css2?family=Saira+Semi+Condensed:wght@500;600;700&family=Arimo:wght@400&display=swap" rel="stylesheet">
<style>
  :root {
    --green: #7dc41f;
    --green-dark: #5e9c12;
    --charcoal: #3a3b3c;
    --ink: #2f3033;
    --paper: #ffffff;
    --stage: #d9d6d1;
  }
  * { box-sizing: border-box; margin: 0; padding: 0; }
  html, body { width: 1200px; height: 825px; overflow: hidden; }
  body {
    background: var(--stage);
    font-family: "Arimo", Arial, sans-serif;
    color: var(--ink);
    position: relative;
  }
  .flyer {
    position: absolute;
    top: 67px;
    width: 492px;
    height: 693px;
    background: var(--paper);
    overflow: hidden;
    box-shadow: 0 4px 14px rgba(0,0,0,.25);
  }
  .flyer--front { left: 80px; }
  .flyer--back { left: 626px; }
  .flyer__art { position: absolute; inset: 0; width: 492px; height: 693px; }
  .abs { position: absolute; white-space: nowrap; }
  .display { font-family: "Saira Semi Condensed", "Arial Narrow", sans-serif; }

  /* svg display type */
  .svg-display { font-family: "Saira Semi Condensed", "Arial Narrow", sans-serif; font-weight: 600; }
  .svg-wordmark { font-family: "Saira Semi Condensed", "Arial Narrow", sans-serif; font-weight: 700; fill: var(--charcoal); }
  .badge-years { font-size: 30px; }
  .badge-label { font-size: 26px; }

  /* front */
  .front__headline { left: 27px; top: 384px; color: var(--green); font-size: 38px; font-weight: 500; line-height: 1; }
  .front__sub { left: 27px; top: 428px; font-size: 19px; color: var(--ink); }
  .front__address { left: 27px; top: 563px; font-size: 15px; line-height: 1.35; color: var(--ink); }
  .perks { right: 24px; top: 330px; list-style: none; text-align: right; color: var(--paper); font-size: 14.5px; line-height: 1.22; }
  .perks li::after {
    content: ""; display: inline-block; width: 8px; height: 8px; border-radius: 50%;
    background: var(--green); margin-left: 8px; vertical-align: middle;
  }
  .front__call { left: 260px; top: 431px; color: var(--paper); font-size: 20px; line-height: 1.2; letter-spacing: .3px; }

  /* back */
  .back__tagline { left: 22px; top: 126px; color: var(--green-dark); font-size: 16.5px; line-height: 1.22; }
  .contact-pill {
    right: 18px; top: 345px; width: 275px; height: 36px;
    background: var(--green); border: 3px solid var(--charcoal); border-right: none;
    border-radius: 18px 0 0 18px;
    font-size: 17px; color: var(--charcoal); display: flex; align-items: center; padding-left: 16px;
    font-family: "Saira Semi Condensed", "Arial Narrow", sans-serif; font-weight: 500;
  }
  .back__story { left: 24px; right: 26px; top: 408px; font-size: 14.5px; line-height: 1.38; color: #4a4b4d; text-align: right; white-space: normal; }
  .back__web { left: 0; right: 0; top: 603px; text-align: center; font-size: 14px; letter-spacing: 2.4px; color: var(--charcoal); }
</style>
</head>
<body>

<!-- FRONT -->
<section class="flyer flyer--front" aria-label="Flyer front">
  <svg class="flyer__art" viewBox="0 0 492 693">
    <defs>
      <radialGradient id="frontPaper" cx="30%" cy="60%" r="70%">
        <stop offset="0" stop-color="#ffffff"/>
        <stop offset="1" stop-color="#dcdddd"/>
      </radialGradient>
      <linearGradient id="frontPhoto" x1="0" y1="0" x2="1" y2="1">
        <stop offset="0" stop-color="#4f6f9a"/>
        <stop offset=".45" stop-color="#6d9a3e"/>
        <stop offset="1" stop-color="#2f5424"/>
      </linearGradient>
      <radialGradient id="basketPhoto" cx="50%" cy="55%" r="55%">
        <stop offset="0" stop-color="#a57a47"/>
        <stop offset="1" stop-color="#3a3b3c" stop-opacity="0"/>
      </radialGradient>
      <linearGradient id="grass" x1="0" y1="0" x2="0" y2="1">
        <stop offset="0" stop-color="#9fdc3a" stop-opacity="0"/>
        <stop offset=".5" stop-color="#8ccf2a"/>
        <stop offset="1" stop-color="#5ea616"/>
      </linearGradient>
    </defs>
    <rect width="492" height="693" fill="url(#frontPaper)"/>
    <path role="img" aria-label="Photo of a gardener planting flowers into a pot" fill="url(#frontPhoto)"
          d="M0 0H492V238C410 262 330 252 250 250C170 248 90 258 0 268Z"/>
    <path d="M0 268C90 258 170 248 250 250C330 252 410 262 492 238V262C400 272 320 262 240 262C150 262 80 276 0 298Z" fill="var(--green)"/>
    <path d="M0 298C80 276 150 262 240 262C320 262 400 272 492 262V272C400 280 320 272 240 274C150 276 80 290 0 310Z" fill="#ffffff"/>
    <path d="M271 270C242 310 228 370 228 430C228 530 246 610 276 665H284C254 610 238 530 238 430C238 370 252 310 281 270Z" fill="var(--green)"/>
    <path d="M281 270C252 310 238 370 238 430C238 530 254 610 284 665H492V268Z" fill="var(--charcoal)"/>
    <rect x="230" y="420" width="262" height="70" fill="var(--green)"/>
    <ellipse role="img" aria-label="Photo of a wicker basket filled with garden hand tools and gloves" cx="370" cy="580" rx="90" ry="72" fill="url(#basketPhoto)"/>
    <rect role="img" aria-label="Illustration of a strip of green grass" x="0" y="610" width="492" height="60" fill="url(#grass)"/>
    <rect x="0" y="668" width="492" height="25" fill="var(--green)"/>

    <g class="badge">
      <circle cx="118" cy="282" r="86" fill="#000" opacity=".12"/>
      <circle cx="118" cy="280" r="82" fill="var(--green)" stroke="#ffffff" stroke-width="6"/>
      <text class="svg-display badge-years" x="118" y="278" text-anchor="middle" fill="#ffffff" textLength="108" lengthAdjust="spacingAndGlyphs">7+ YEARS</text>
      <text class="svg-display badge-label" x="118" y="310" text-anchor="middle" fill="#ffffff" textLength="112" lengthAdjust="spacingAndGlyphs">EXPERIENCE</text>
    </g>

    <g class="wordmark" aria-label="Marlow Yardcraft">
      <text class="svg-wordmark" x="27" y="508" font-size="40" textLength="150" lengthAdjust="spacingAndGlyphs">MARLOW</text>
      <text class="svg-wordmark" x="27" y="540" font-size="34" textLength="190" lengthAdjust="spacingAndGlyphs">YARDCRAFT</text>
    </g>
  </svg>

  <ul class="perks abs">
    <li>7+ years experience</li>
    <li>Attention to detail</li>
    <li>Creative vision</li>
    <li>Servicing Marlow metro areas</li>
  </ul>

  <p class="front__call abs display">CONTACT US NOW!<br>CALL: 08 6341 2705</p>

  <p class="front__headline abs">Get your</p>
  <p class="front__sub abs">free quote today</p>
  <p class="front__address abs">Level 12, 40 Harrow Street,<br>Marlow, WA 6100</p>
</section>

<!-- BACK -->
<section class="flyer flyer--back" aria-label="Flyer back">
  <svg class="flyer__art" viewBox="0 0 492 693">
    <defs>
      <radialGradient id="backPaper" cx="50%" cy="45%" r="70%">
        <stop offset="0" stop-color="#ffffff"/>
        <stop offset="1" stop-color="#dfe0e0"/>
      </radialGradient>
      <linearGradient id="mowerPhoto" x1="0" y1="0" x2="0" y2="1">
        <stop offset="0" stop-color="#5f8a2e"/>
        <stop offset=".55" stop-color="#34465f"/>
        <stop offset="1" stop-color="#6fae2c"/>
      </linearGradient>
      <linearGradient id="parkPhoto" x1="0" y1="0" x2="0" y2="1">
        <stop offset="0" stop-color="#d9e98a"/>
        <stop offset=".45" stop-color="#3f6a1f"/>
        <stop offset="1" stop-color="#8fcf3a"/>
      </linearGradient>
      <linearGradient id="grassBack" x1="0" y1="0" x2="0" y2="1">
        <stop offset="0" stop-color="#9fdc3a" stop-opacity="0"/>
        <stop offset=".5" stop-color="#8ccf2a"/>
        <stop offset="1" stop-color="#5ea616"/>
      </linearGradient>
    </defs>
    <rect width="492" height="693" fill="url(#backPaper)"/>
    <path d="M0 0H240C228 80 220 170 160 232C110 238 50 240 0 236Z" fill="#ffffff"/>
    <path d="M236 0H250C240 90 230 180 172 238L150 240C210 178 226 80 236 0Z" fill="var(--green)"/>
    <path d="M0 222C60 228 110 228 150 226L160 240C110 246 50 246 0 240Z" fill="var(--green)"/>
    <path role="img" aria-label="Photo of a gardener mowing a lawn in front of a hedge"
          fill="url(#mowerPhoto)" d="M250 0H492V212C400 220 280 228 172 238C230 180 240 90 250 0Z"/>
    <path d="M0 240C150 240 320 220 492 212V232C330 240 160 258 0 270Z" fill="var(--charcoal)"/>
    <path d="M0 270C160 258 330 240 492 232V242C330 250 160 268 0 282Z" fill="#ffffff"/>
    <rect role="img" aria-label="Photo of a sunlit park with tall trees and green lawn" x="0" y="481" width="492" height="112" fill="url(#parkPhoto)"/>
    <rect x="0" y="478" width="492" height="3" fill="var(--green)"/>
    <rect role="img" aria-label="Illustration of a strip of green grass" x="0" y="620" width="492" height="50" fill="url(#grassBack)"/>
    <rect x="0" y="668" width="492" height="25" fill="var(--charcoal)"/>

    <g class="wordmark" aria-label="Marlow Yardcraft">
      <text class="svg-wordmark" x="22" y="70" font-size="42" textLength="150" lengthAdjust="spacingAndGlyphs">MARLOW</text>
      <text class="svg-wordmark" x="22" y="104" font-size="36" textLength="190" lengthAdjust="spacingAndGlyphs">YARDCRAFT</text>
    </g>

    <g class="badge">
      <circle cx="104" cy="300" r="82" fill="#000" opacity=".12"/>
      <circle cx="104" cy="298" r="76" fill="var(--charcoal)" stroke="#ffffff" stroke-width="5"/>
      <text class="svg-display badge-years" x="104" y="294" text-anchor="middle" fill="var(--green)" textLength="106" lengthAdjust="spacingAndGlyphs">7+ YEARS</text>
      <text class="svg-display badge-label" x="104" y="325" text-anchor="middle" fill="#ffffff" textLength="112" lengthAdjust="spacingAndGlyphs">EXPERIENCE</text>
    </g>

    <g class="promise">
      <text class="svg-wordmark" x="471" y="293" font-size="25" text-anchor="end" fill="var(--green)" style="fill:var(--green)" textLength="259" lengthAdjust="spacingAndGlyphs">LET US DO THE HARD WORK</text>
      <text class="svg-display" x="471" y="313" font-size="16" text-anchor="end" fill="var(--ink)" textLength="259" lengthAdjust="spacingAndGlyphs">SO THAT YOU CAN ENJOY YOUR GARDEN</text>
    </g>
  </svg>

  <p class="back__tagline abs">Reliable, affordable<br>gardening services<br>in Marlow</p>
  <p class="contact-pill abs">CONTACT US: 08 6341 2705</p>
  <p class="back__story abs">Here at Marlow Yardcraft, we’re proud to have built a reputation as a versatile landscape gardening company that delivers professional service and high quality results.</p>
  <p class="back__web abs">www.yardcraft-marlow.com.au</p>
</section>

</body>
</html>
```